Sports medicine multidisciplinary brochures

Multi-disciplinary sports medicine clinic. Need a range of pamphlet / foldable brochures to advertise our various services. Looking at keeping a similar 'look' between the various brochures to still ID as being part of the group, but perhaps slight colour variation / different front pic to distinguish them. Looking at a pamphlet for: 1) General clinic (about us) info 2) Concussion info 3) Podiatry 4) Sports Physicians 5) Exercise Physiology 6) Osteoarthritis 7) Physiotherapy. Modern feel, but still warm / inviting. See attached logo / cards / etc. Thank you!

Target Market(s)

Athletes, sports injuries + general health / medical

Industry/Entity Type

Clinic

Requirements
Nice to have
• Simple, warm design. Activity / health / lifestyle related feel.
• Design to allow easy adaptation of wording / content.

```html
<!DOCTYPE html>
<html lang="en">
<head>
<meta charset="utf-8">
<title>Kineta – Concussion Management Brochure</title>
<link href="https://fonts.googleapis.com/css2?family=Anton&family=Oswald:wght@500;600&family=Montserrat:ital,wght@0,400;0,600;0,700;1,500&display=swap" rel="stylesheet">
<style>
:root{
  --orange:#f07f1e;
  --orange-light:#f7a43f;
  --orange-deep:#e0661a;
  --green:#1f9a54;
  --green-deep:#137a40;
  --white:#ffffff;
  --ink:#333333;
  --backdrop:#e4e4e4;
}
*{box-sizing:border-box;margin:0;padding:0}
html,body{width:1200px;height:1200px;overflow:hidden}
body{background:var(--backdrop);font-family:'Montserrat',sans-serif;position:relative}
.spread{position:absolute;left:210px;width:780px;height:552px;background:var(--white);overflow:hidden;box-shadow:0 6px 18px rgba(0,0,0,.25)}
.spread--outside{top:40px}
.spread--inside{top:612px}
.spread__shapes,.photo{position:absolute}
.spread__shapes{left:0;top:0;width:780px;height:552px}
.photo-panel{position:absolute;border-radius:10px}
.photo-panel--sprinter{left:18px;top:330px;width:226px;height:200px;background:linear-gradient(160deg,#f58d2e 0%,#d9621a 100%);box-shadow:inset 0 0 0 1px rgba(255,255,255,.25)}
.photo-panel--pushup{left:18px;top:402px;width:226px;height:104px;background:linear-gradient(160deg,#f1f1f1 0%,#cfd3d6 100%)}
.fold{position:absolute;top:0;width:1px;height:552px;background:rgba(0,0,0,.08)}
.block{position:absolute;font-size:7px;line-height:1.38}
.heading{font-family:'Oswald',sans-serif;font-weight:600;font-size:15px;line-height:1.1;margin-bottom:6px}
ul{list-style:none}
li{position:relative;padding-left:8px;margin-bottom:3px}
li::before{content:"";position:absolute;left:0;top:3px;width:4px;height:4px;border-radius:50%;background:currentColor}
.bul-green li::before{background:var(--green)}
.bul-orange li::before{background:var(--orange)}
.sub{margin-left:8px;color:#d9f5c8}
p{margin-bottom:5px}
.brand{display:flex;align-items:center;gap:6px;font-weight:700;color:var(--green);letter-spacing:2px}
.brand__dot{width:12px;height:12px;border-radius:50%;background:var(--orange)}
.brand__tag{font-size:5.5px;letter-spacing:1.2px;color:var(--orange);font-weight:600;margin-top:2px}
.title{position:absolute;left:540px;top:452px;width:230px;text-align:center;line-height:.95}
.title__main{font-family:'Anton',sans-serif;font-size:44px;color:var(--white);letter-spacing:.5px}
.title__sub{font-family:'Anton',sans-serif;font-size:28px;color:var(--orange);letter-spacing:.5px}
.contact{color:var(--white)}
.contact__row{display:flex;gap:5px;align-items:flex-start;margin-bottom:3px}
.contact__row svg{flex:none;margin-top:1px}
.hours{color:var(--white)}
.hours li{border-bottom:1px solid rgba(255,255,255,.7);padding-bottom:4px;margin-bottom:6px;width:150px}
.label-green{color:var(--green-deep);font-family:'Oswald',sans-serif;font-weight:600;font-size:9px;letter-spacing:.3px;margin:6px 0 4px}
.intro-italic{font-style:italic;font-weight:500}
</style>
</head>
<body>

<!-- Outside spread -->
<section class="spread spread--outside" aria-label="Brochure outside">
  <svg class="spread__shapes" viewBox="0 0 780 552" aria-hidden="true">
    <rect x="0" y="0" width="520" height="552" fill="var(--orange)"/>
    <path d="M405,0 C345,130 505,210 470,330 C445,430 490,500 505,552 L520,552 L520,0 Z" fill="var(--orange-light)"/>
    <path d="M430,0 C395,70 440,150 520,170 L520,0 Z" fill="var(--white)"/>
    <path d="M700,0 L780,0 L780,120 C765,70 740,30 700,0 Z" fill="var(--green)"/>
    <path d="M690,0 L700,0 C740,30 765,70 780,120 L780,132 C760,78 735,35 690,0 Z" fill="var(--orange)"/>
  </svg>
  <svg class="photo" style="left:430px;top:0" width="90" height="170" role="img" aria-label="Photo: physiotherapist assisting a patient with a shoulder stretch">
    <defs><linearGradient id="g1" x1="0" y1="0" x2="0" y2="1"><stop offset="0" stop-color="#f3ece6"/><stop offset="1" stop-color="#d8b7a4"/></linearGradient></defs>
    <path d="M0,0 C-35,70 10,150 90,170 L90,0 Z" fill="url(#g1)"/>
  </svg>
  <svg class="photo" style="left:520px;top:120px" width="260" height="330" role="img" aria-label="Photo: female athlete sprinting on a beach under a cloudy sky">
    <defs><linearGradient id="g2" x1="0" y1="0" x2="0" y2="1"><stop offset="0" stop-color="#dfe7ee"/><stop offset=".65" stop-color="#a9bccb"/><stop offset="1" stop-color="#c7b08e"/></linearGradient></defs>
    <path d="M0,30 C80,40 160,20 260,0 L260,200 C180,230 90,280 0,320 Z" fill="url(#g2)"/>
  </svg>
  <svg class="spread__shapes" viewBox="0 0 780 552" aria-hidden="true">
    <path d="M520,428 C600,392 700,350 780,318 L780,332 C700,362 600,404 520,442 Z" fill="var(--orange)"/>
    <path d="M520,442 C600,404 700,362 780,332 L780,552 L520,552 Z" fill="var(--green)"/>
  </svg>
  <div class="photo-panel photo-panel--sprinter" role="img" aria-label="Photo: male sprinter in silhouette driving forward from a start"></div>
  <svg class="photo" style="left:402px;top:424px" width="96" height="96" role="img" aria-label="Street map showing the clinic location">
    <circle cx="48" cy="48" r="45" fill="#eeeeee" stroke="var(--white)" stroke-width="4"/>
    <circle cx="48" cy="48" r="47" fill="none" stroke="var(--orange-deep)" stroke-width="1.5"/>
  </svg>
  <div class="fold" style="left:260px"></div><div class="fold" style="left:520px"></div>

  <div class="block" style="left:18px;top:20px;width:225px;color:var(--white)">
    <div class="heading"><span>Early</span> <span style="color:var(--green-deep)">management</span></div>
    <ul>
      <li>Rest – the most important early treatment
        <div class="sub">• Both physical rest as well as mental rest (screens, reading, games) can worsen symptoms and should be limited</div></li>
      <li>Non-urgent review with your sports physician at Kineta
        <div class="sub">• Within 1–2 days after your concussion is best</div></li>
      <li>Paracetamol if you have a headache.</li>
      <li>Your sports physician will then develop a plan to return to school, work, and / or sport safely.</li>
      <li>Further testing such as advanced computer based reaction tests may also be undertaken to better assess your condition.</li>
      <li>Clearance by your sports physician before returning to full training and competition.</li>
    </ul>
    <p style="margin-top:6px">Caring for your brain is vital, and as Sports and Exercise Physicians we are dedicated to making sure that up to date guidelines and best medical management are followed to get you safely back to work, school, and sport, as well as preventing any long-term issues.</p>
  </div>

  <div class="block" style="left:272px;top:196px;width:240px">
    <div class="brand" style="font-size:20px"><span class="brand__dot"></span>KINETA</div>
    <div class="label-green" style="margin-top:4px">KINETA MOTION &amp; JOINT CLINIC</div>
    <div class="contact">
      <div class="contact__row"><svg width="7" height="7" viewBox="0 0 10 10"><path d="M2,0 L4,2.5 L3,4 C4,6 5,7 6,7 L7.5,6 L10,8 L8.5,10 C4,10 0,6 0,1.5 Z" fill="#fff"/></svg>08 5550 1234</div>
      <div class="contact__row"><svg width="7" height="7" viewBox="0 0 10 10"><rect x="0" y="1.5" width="10" height="7" fill="none" stroke="#fff" stroke-width="1.3"/><path d="M0,2 L5,6 L10,2" fill="none" stroke="#fff" stroke-width="1.3"/></svg>info@kinetaclinic.example</div>
      <div class="contact__row"><svg width="7" height="8" viewBox="0 0 10 12"><path d="M5,0 C8,0 10,2 10,5 C10,8 5,12 5,12 C5,12 0,8 0,5 C0,2 2,0 5,0 Z" fill="#fff"/><circle cx="5" cy="4.5" r="1.7" fill="var(--orange)"/></svg>Kineta Motion &amp; Joint Clinic<br>12 Harbour Rd, Westbrook 5099</div>
      <div class="contact__row"><svg width="7" height="7" viewBox="0 0 10 10"><circle cx="5" cy="5" r="4.3" fill="none" stroke="#fff" stroke-width="1.3"/><path d="M0.7,5 H9.3 M5,0.7 V9.3" stroke="#fff" stroke-width="1"/></svg>www.kinetaclinic.example</div>
    </div>
    <div class="label-green">OPENING HOURS</div>
    <ul class="hours">
      <li>Monday – Wednesday 8:30 - 6</li>
      <li>Thursday 8:30 - 8</li>
      <li>Friday 8:30 - 3</li>
      <li>Saturday 9 - 12:30</li>
    </ul>
  </div>

  <div class="block" style="left:520px;top:40px;width:260px;display:flex;flex-direction:column;align-items:center">
    <div class="brand" style="font-size:24px"><span class="brand__dot"></span>KINETA</div>
    <div class="brand__tag">MOTION &amp; JOINT CLINIC</div>
  </div>
  <div class="title"><div class="title__main">CONCUSSION</div><div class="title__sub">MANAGEMENT</div></div>
</section>

<!-- Inside spread -->
<section class="spread spread--inside" aria-label="Brochure inside">
  <svg class="spread__shapes" viewBox="0 0 780 552" aria-hidden="true">
    <path d="M0,0 H260 V120 C180,130 80,150 0,205 Z" fill="var(--orange)"/>
    <path d="M0,198 C80,145 180,124 260,112 L260,124 C180,136 80,158 0,212 Z" fill="var(--orange)"/>
    <path d="M0,212 C80,158 180,136 260,124 L260,320 C190,378 90,388 0,372 Z" fill="var(--green)"/>
    <path d="M0,372 C90,388 190,378 260,320 L260,332 C190,390 90,400 0,384 Z" fill="var(--orange)"/>
    <path d="M430,0 H520 V95 C480,70 450,35 430,0 Z" fill="var(--green)"/>
    <path d="M420,0 H430 C450,35 480,70 520,95 V105 C475,78 442,40 420,0 Z" fill="var(--orange)"/>
  </svg>
  <svg class="photo" style="left:520px;top:0" width="260" height="165" role="img" aria-label="Photo: doctor examining an athlete's knee in a clinic">
    <defs><linearGradient id="g3" x1="0" y1="0" x2="1" y2="1"><stop offset="0" stop-color="#f4f4f4"/><stop offset="1" stop-color="#cfd6dc"/></linearGradient></defs>
    <rect width="260" height="165" fill="url(#g3)"/>
  </svg>
  <svg class="photo" style="left:320px;top:14px" width="130" height="130" role="img" aria-label="Photo: physiotherapist guiding a patient through a resistance band exercise">
    <defs><linearGradient id="g4" x1="0" y1="0" x2="0" y2="1"><stop offset="0" stop-color="#f2eee9"/><stop offset="1" stop-color="#d9c2b0"/></linearGradient></defs>
    <circle cx="65" cy="65" r="58" fill="url(#g4)" stroke="var(--white)" stroke-width="3"/>
    <circle cx="65" cy="65" r="62" fill="none" stroke="var(--orange)" stroke-width="4"/>
  </svg>
  <div class="photo-panel photo-panel--pushup" role="img" aria-label="Photo: athlete doing push-ups on a medicine ball"></div>
  <svg class="spread__shapes" viewBox="0 0 780 552" role="img" aria-label="Photo: sprinter in the starting blocks on a track, green toned">
    <defs><linearGradient id="g5" x1="0" y1="0" x2="1" y2="0"><stop offset="0" stop-color="#2fae66"/><stop offset=".7" stop-color="#137a40"/><stop offset="1" stop-color="#0d5e31"/></linearGradient></defs>
    <path d="M0,526 C100,520 200,512 260,506 C400,456 600,410 780,372 V384 C600,422 400,468 260,518 C200,524 100,532 0,538 Z" fill="var(--orange)"/>
    <path d="M0,538 C100,532 200,524 260,518 C400,468 600,422 780,384 V552 H0 Z" fill="url(#g5)"/>
  </svg>
  <div class="fold" style="left:260px"></div><div class="fold" style="left:520px"></div>

  <div class="block" style="left:18px;top:16px;width:228px;color:var(--white);font-size:6.4px">
    <div class="heading" style="color:var(--green-deep)">Concussion Management</div>
    <p>Concussion is a complex and evolving functional injury to the brain. Prompt trained medical review is mandatory in all international guidelines, as well as before returning to sport. This is to ensure there is no evidence of structural or other major pathology, as well as to guide you back to normal life and sport safely. Careful monitoring by your specialist Sport and Exercise Physicians at Kineta, trained in up to date concussion management, will help guide this process to the same standard of care whether you had a fall at work, are a 12-year-old soccer player, or an elite athlete. You only have one brain and we believe the same standard of care applies wherever you may be.</p>
  </div>
  <div class="block" style="left:20px;top:214px;width:210px;color:var(--white);font-size:6.4px">
    <p class="intro-italic">While concussion itself is a largely benign condition that typically fully resolves within 7–10 days (90% of people), there are important factors to be aware of:</p>
    <ul class="bul-orange" style="margin-top:6px">
      <li>Concussion can occur with a sudden impact to the body, not just to the head</li>
      <li>Concussion often occurs without loss of consciousness</li>
      <li>After a concussion, you cannot return to sport or activity on the same day</li>
      <li>Symptoms evolve over time, and therefore you may experience different symptoms at different times</li>
    </ul>
  </div>

  <div class="block bul-orange" style="left:276px;top:158px;width:230px;color:var(--ink);font-size:6.6px">
    <ul>
      <li>Our brain has many different functions and concussion can affect any or all these areas but typically you may notice:</li>
    </ul>
    <ul style="margin-left:8px">
      <li>Headache</li>
      <li>Lethargy as well as sleep disturbances</li>
      <li>Balance difficulties and dizziness</li>
      <li>Disorientation and concentration issues</li>
      <li>Temporary loss of memory</li>
      <li>Mood changes such as being more irritable or emotional than usual</li>
      <li>Blurred vision</li>
    </ul>
    <p style="margin-top:8px">Given these changes, it is important that you do not drive during this time, nor put yourself in risky situations as your judgement and reflexes are compromised.</p>
    <p>No alcohol, sleeping tablets, aspirin, or anti-inflammatory medications.</p>
  </div>

  <div class="block bul-orange" style="left:536px;top:180px;width:230px;color:var(--orange-deep);font-size:6.6px">
    <p class="intro-italic">While extremely rare, it is important to watch for the following signs that potentially can indicate more serious issues. If any of these signs are noticed, please contact your doctor or the nearest emergency department.</p>
    <ul style="margin-top:6px">
      <li>Frequent vomiting and severe headaches</li>
      <li>Excessive drowsiness or falls unconscious</li>
      <li>Convulsions or spasms</li>
      <li>Weakness and slurred speech</li>
      <li>Or if you simply remain concerned about any further deterioration in symptoms</li>
    </ul>
  </div>
</section>

</body>
</html>
```